Create a Dynamic, Connecting, Professional looking PowerPoint Design master for our company.

Power point design

Target Market: High worth individuals and corporate group
Industry: Sport and services

Landscape format

Should include various slide such as:
Introduction page (photo background- inclusive logo)
Company presentation (with photos of various projects)
Different slide layouts to place general information with large photo & logo (in different sizes) as well as standard elements, such as text boxes, lines, default shapes, etc
Timeline page
Table pages
Various infographic style pages with editable chart
Our service page – Icons
Location page (world map)
Comparaison pages (3 offers to compare)
Closing page – thank you & contact
Page numbering

Colors:
#6ea6fa
#517ed8
#3758b4
#203390
#060d6c
#2EC193
White / Grey and black

Fonts:
Work sans / Helveticanow / Or other suitable.
Creative use of the logo in the slides. The Timrel icon may be used as a small device or large watermark to enhance branding.

The uploaded photos are indicative of the ones that we would like to use (ie: sail racing) there are here for you to include in the design but would need to be easily replaceable by the final photos we would be using.

If you have any questions or need any aditional material, please send me a message and I will try to respond to it as quickly as possible (bearing in mind that my time zone is UTC +2)

Target Market(s)

High worth individuals and corporate groups

Industry/Entity Type

Sport and services (sailing)

Font styles to use
Other font styles liked:
• Work Sans / Helveticanow

Colors
0054AA
0677BA
7BADD7
CADEEF
E8F1F8
00AB8E
00BBA5
67D7C9
C6EFE9
E9F9F6

Requirements
Must have
• Introduction page (photo background- inclusive logo) Company presentation (with photos of various projects) Different slide layouts to place general information with large photo & logo (in different sizes) as well as standard elements, such as text boxes, lines, default shapes, etc Timeline page Table pages Various infographic style pages with editable chart Our service page – Icons Location page (world map) Comparaison pages (3 offers to compare) Closing page – thank you & contact Page numbering
Nice to have
• Creative use of the logo in the slides. The Timrel icon may be used as a small device or large watermark to enhance branding.

```html
<!DOCTYPE html>
<html lang="en">
<head>
<meta charset="utf-8">
<title>Timrel – Presentation Master Overview</title>
<link href="https://fonts.googleapis.com/css2?family=Work+Sans:wght@400;500;600;700;800&family=Roboto:wght@400;500;700&display=swap" rel="stylesheet">
<style>
  :root{
    --board:#8d8d8d;
    --navy:#0a2f6b;
    --deep:#0054aa;
    --mid:#0677ba;
    --sky:#7badd7;
    --pale:#cadeef;
    --mist:#e8f1f8;
    --teal:#00ab8e;
    --teal-2:#2ec193;
    --teal-pale:#c6efe9;
    --white:#ffffff;
    --ink:#243447;
    --grey:#6c7a89;
  }
  *{box-sizing:border-box;margin:0;padding:0}
  html,body{width:732px;height:1200px;overflow:hidden}
  body{background:var(--board);font-family:"Work Sans",Arial,sans-serif;position:relative;color:var(--ink)}
  .slide{position:absolute;width:336px;height:183px;overflow:hidden;background:linear-gradient(135deg,var(--mist),#d3e8f5);box-shadow:0 1px 3px rgba(0,0,0,.35)}
  .col-a{left:22px}.col-b{left:374px}
  .row-1{top:18px}.row-2{top:213px}.row-3{top:408px}.row-4{top:603px}.row-5{top:798px}.row-6{top:993px}
  .wave{position:absolute;inset:0;width:100%;height:100%}
  .title{position:absolute;font-family:"Roboto",Arial,sans-serif;font-weight:500;color:var(--white);font-size:19px;letter-spacing:.2px}
  .title.dark{color:var(--navy)}
  .brand{position:absolute;display:flex;align-items:center;gap:3px;font-weight:800;font-size:9px;color:var(--navy);letter-spacing:.5px}
  .brand i{width:7px;height:7px;border-radius:50%;background:var(--navy);display:block}
  .brand.light{color:var(--white)}.brand.light i{background:var(--white)}
  .pager{position:absolute;right:4px;bottom:10px;width:9px;display:flex;flex-direction:column;gap:2px;align-items:center}
  .pager span{width:4px;height:4px;background:var(--white);opacity:.85}
  .photo{position:absolute;background:linear-gradient(160deg,#8fb4cf,#3d6d92 55%,#1f4566)}
  .photo.sea{background:linear-gradient(180deg,#a9c9de,#4b82ab 50%,#1d4d7c)}
  .photo.sail{background:linear-gradient(170deg,#dfe9f0,#9ab7cc 45%,#2f5f86)}
  .txt{position:absolute;font-size:4.5px;line-height:1.45;color:var(--ink)}
  .txt.light{color:var(--white)}
  .label{position:absolute;font-size:6px;font-weight:600;color:var(--navy)}

  /* cover */
  .cover-name{position:absolute;left:22px;top:40px;display:flex;align-items:center;gap:8px;font-size:44px;font-weight:800;color:var(--navy);letter-spacing:1px}
  .cover-name i{width:22px;height:22px;border-radius:50%;background:var(--navy);display:block}
  .cover-sub{position:absolute;left:60px;top:95px;font-size:8px;letter-spacing:8px;color:var(--mid);font-weight:500}

  /* company */
  .info-panel{position:absolute;left:10px;top:40px;width:90px;height:70px;background:var(--deep);padding:6px}
  /* table */
  .data-table{position:absolute;left:10px;top:44px;width:300px;border-collapse:collapse;font-size:4.5px;font-family:"Roboto",Arial,sans-serif}
  .data-table th{background:var(--teal);color:var(--white);font-weight:500;padding:3px 4px;text-align:left}
  .data-table td{padding:2.6px 4px;border-bottom:1px solid #d6e4ef;background:var(--white)}
  .data-table tr:nth-child(even) td{background:#eef5fa}

  /* location */
  .map{position:absolute;left:30px;top:40px;width:240px;height:90px;background:radial-gradient(ellipse at 50% 50%,#9bc8e4,#c5e0f0 70%);border-radius:40%}
  .pin{position:absolute;width:10px;height:14px}
  .track{position:absolute;left:20px;right:20px;top:150px;height:1px;background:var(--mid)}
  .track-dot{position:absolute;top:147px;width:7px;height:7px;border-radius:50%;background:var(--white);border:1.5px solid var(--mid)}

  /* growth */
  .stat{position:absolute;background:var(--teal);color:var(--white);font-size:5px;padding:3px 5px;font-weight:600}
  /* cards */
  .card{position:absolute;top:58px;width:64px;height:88px;background:rgba(255,255,255,.55);border:1px solid rgba(255,255,255,.8)}
  .card.active{background:var(--teal);}
  .card .icon{position:absolute;left:20px;top:10px;width:24px;height:24px;border-radius:50%;background:var(--teal);display:flex;align-items:center;justify-content:center}
  .card.active .icon{background:var(--white)}
  .card .head{position:absolute;top:42px;width:100%;text-align:center;font-size:5.5px;font-weight:600;color:var(--navy)}
  .card.active .head,.card.active .txt{color:var(--white)}
  .card .txt{left:6px;right:6px;top:52px;text-align:center}
  /* services */
  .svc{position:absolute;top:56px;width:90px}
  .svc .icon{width:18px;height:18px;border-radius:3px;background:var(--teal);display:flex;align-items:center;justify-content:center}
  .band{position:absolute;left:0;right:0;bottom:0;height:42px;background:linear-gradient(90deg,var(--teal),var(--teal-2))}
  /* timeline */
  .boat{position:absolute;background:linear-gradient(180deg,var(--navy),#123a78);clip-path:polygon(50% 0,100% 85%,0 85%,0 100%,100% 100%,100% 85%)}
  .year{position:absolute;font-size:6px;font-weight:700;color:var(--navy)}
  /* contact */
  .contact-row{position:absolute;left:218px;display:flex;align-items:center;gap:4px;font-size:4.5px;color:var(--white)}
  .contact-row b{width:9px;height:9px;border-radius:50%;background:var(--white);display:flex;align-items:center;justify-content:center}
  /* closing */
  .thanks{position:absolute;left:0;right:0;top:110px;text-align:center;font-family:"Roboto",Arial,sans-serif;font-size:26px;font-weight:700;color:var(--white);letter-spacing:3px}
  .site{position:absolute;left:0;right:0;top:142px;text-align:center;font-size:6px;color:var(--white);letter-spacing:1.5px}
  .board-note{position:absolute;left:430px;top:1085px;font-size:11px;color:#1b1b1b;font-family:"Work Sans",Arial,sans-serif}
</style>
</head>
<body>

<!-- 1 Welcome -->
<section class="slide col-a row-1">
  <svg class="wave" viewBox="0 0 336 183" preserveAspectRatio="none">
    <path d="M0 0H336V183H0Z" fill="#e6f3fa"/>
    <path d="M180 0C230 40 200 90 260 120S336 140 336 183V0Z" fill="#7badd7" opacity=".6"/>
    <path d="M230 0C260 50 240 110 300 140L336 150V0Z" fill="#0677ba" opacity=".75"/>
    <path d="M0 150C80 120 160 170 240 150S336 160 336 183H0Z" fill="#cadeef"/>
    <path d="M0 165C100 150 200 185 336 165V183H0Z" fill="#0677ba" opacity=".8"/>
  </svg>
  <div class="cover-name"><i></i>TIMREL</div>
  <div class="cover-sub">WELCOME</div>
  <div class="pager"><span></span><span></span><span></span></div>
</section>

<!-- 2 Introduction -->
<section class="slide col-b row-1">
  <svg class="wave" viewBox="0 0 336 183" preserveAspectRatio="none">
    <path d="M0 0H336V183H0Z" fill="#e8f1f8"/>
    <path d="M150 0H336V60C280 75 220 45 150 60Z" fill="#0677ba"/>
    <path d="M0 160C90 140 200 180 336 150V183H0Z" fill="#7badd7"/>
  </svg>
  <div class="photo sail" role="img" aria-label="Crew working on deck of a racing yacht" style="left:0;top:0;width:150px;height:120px"></div>
  <div class="title" style="left:160px;top:14px">Introduction</div>
  <p class="txt" style="left:160px;top:72px;width:160px">Our team builds sailing programs for clients who value speed, care and shared success on every regatta we join together across the season.</p>
  <div class="brand" style="left:268px;top:112px"><i></i>TIMREL</div>
  <div class="pager"><span></span><span></span><span></span></div>
</section>

<!-- 3 Company presentation -->
<section class="slide col-a row-2">
  <svg class="wave" viewBox="0 0 336 183" preserveAspectRatio="none">
    <path d="M0 0H336V183H0Z" fill="#d3e8f5"/>
    <path d="M0 0H336V30C250 45 120 20 0 38Z" fill="#0677ba"/>
    <path d="M0 150C100 130 220 175 336 145V183H0Z" fill="#0054aa"/>
  </svg>
  <div class="title" style="left:10px;top:8px">Company presentation</div>
  <div class="info-panel"><p class="txt light" style="position:static">Projects delivered for private owners and corporate crews, from training days to full racing seasons.</p></div>
  <div class="photo sea" role="img" aria-label="Yacht sailing on open water" style="left:110px;top:40px;width:70px;height:58px"></div>
  <div class="photo sail" role="img" aria-label="Two racing yachts under sail" style="left:186px;top:40px;width:70px;height:58px"></div>
  <div class="photo" role="img" aria-label="Yacht heeling in the wind" style="left:110px;top:102px;width:70px;height:42px"></div>
  <p class="txt" style="left:190px;top:105px;width:70px">Short project notes placed beside each image.</p>
  <div class="brand light" style="left:280px;top:12px"><i></i>TIMREL</div>
  <div class="pager"><span></span><span></span><span></span></div>
</section>

<!-- 4 Partner table -->
<section class="slide col-b row-2">
  <svg class="wave" viewBox="0 0 336 183" preserveAspectRatio="none">
    <path d="M0 0H336V183H0Z" fill="#e8f1f8"/>
    <path d="M0 0H336V32C250 44 130 22 0 36Z" fill="#0677ba"/>
    <path d="M0 160C120 145 230 180 336 155V183H0Z" fill="#7badd7"/>
  </svg>
  <div class="title" style="left:10px;top:8px">Partner, Our Main Priority</div>
  <table class="data-table">
    <tr><th>Partner</th><th>Project scope</th><th>Season</th><th>Boats</th><th>Status</th></tr>
    <tr><td>Option A</td><td>Regatta support</td><td>2021</td><td>4</td><td>Active</td></tr>
    <tr><td>Option B</td><td>Crew training</td><td>2021</td><td>2</td><td>Active</td></tr>
    <tr><td>Option C</td><td>Hospitality</td><td>2022</td><td>3</td><td>Planned</td></tr>
    <tr><td>Option D</td><td>Boat delivery</td><td>2022</td><td>1</td><td>Active</td></tr>
    <tr><td>Option E</td><td>Event days</td><td>2023</td><td>5</td><td>Planned</td></tr>
  </table>
  <div class="pager"><span></span><span></span><span></span></div>
</section>

<!-- 5 Location -->
<section class="slide col-a row-3">
  <svg class="wave" viewBox="0 0 336 183" preserveAspectRatio="none">
    <path d="M0 0H336V183H0Z" fill="#cde6f4"/>
    <path d="M0 0H336V30C250 42 120 18 0 34Z" fill="#0677ba"/>
    <path d="M220 0C250 30 300 20 336 50V0Z" fill="#0054aa"/>
  </svg>
  <div class="title" style="left:10px;top:8px">Location</div>
  <div class="map" role="img" aria-label="World map showing sailing venues"></div>
  <svg class="pin" style="left:58px;top:62px" viewBox="0 0 10 14"><path d="M5 0a5 5 0 0 1 5 5c0 4-5 9-5 9S0 9 0 5a5 5 0 0 1 5-5z" fill="#0054aa"/><circle cx="5" cy="5" r="2" fill="#fff"/></svg>
  <svg class="pin" style="left:160px;top:58px" viewBox="0 0 10 14"><path d="M5 0a5 5 0 0 1 5 5c0 4-5 9-5 9S0 9 0 5a5 5 0 0 1 5-5z" fill="#00ab8e"/><circle cx="5" cy="5" r="2" fill="#fff"/></svg>
  <div class="track"></div>
  <div class="track-dot" style="left:40px"></div><div class="track-dot" style="left:110px"></div><div class="track-dot" style="left:180px"></div><div class="track-dot" style="left:250px"></div>
  <div class="brand" style="left:280px;top:38px"><i></i>TIMREL</div>
  <div class="pager"><span></span><span></span><span></span></div>
</section>

<!-- 6 Growth -->
<section class="slide col-b row-3">
  <svg class="wave" viewBox="0 0 336 183" preserveAspectRatio="none">
    <path d="M0 0H336V183H0Z" fill="#d9edf7"/>
    <path d="M0 0H336V30C250 42 120 18 0 34Z" fill="#0677ba"/>
    <path d="M0 160C100 150 220 180 336 158V183H0Z" fill="#7badd7"/>
    <g stroke="#b7d3e6" stroke-width=".6"><path d="M20 150H170M20 125H170M20 100H170M20 75H170"/></g>
    <polyline points="20,140 40,120 58,128 78,100 98,110 118,82 140,92 165,60" fill="none" stroke="#00ab8e" stroke-width="1.8"/>
  </svg>
  <div class="title" style="left:10px;top:8px">Year by Year Growth</div>
  <div class="stat" style="left:70px;top:44px">42%</div>
  <div class="label" style="left:185px;top:48px;font-size:9px">Description</div>
  <p class="txt" style="left:185px;top:62px;width:130px">Growth of fleet and partners since launch, shown as an editable chart.</p>
  <div class="stat" style="left:185px;top:88px">1,250 km</div><div class="stat" style="left:230px;top:88px">+18 boats</div>
  <div class="photo sea" role="img" aria-label="Sailing team on the water" style="left:185px;top:108px;width:130px;height:42px"></div>
  <div class="brand light" style="left:280px;top:12px"><i></i>TIMREL</div>
  <div class="pager"><span></span><span></span><span></span></div>
</section>

<!-- 7 Value to user -->
<section class="slide col-a row-4">
  <svg class="wave" viewBox="0 0 336 183" preserveAspectRatio="none">
    <path d="M0 0H336V183H0Z" fill="#c8e4f1"/>
    <path d="M0 0H336V30C250 42 120 18 0 34Z" fill="#0677ba"/>
  </svg>
  <div class="title" style="left:10px;top:8px">Value to user</div>
  <div class="card" style="left:16px"><div class="icon"><svg width="12" height="12" viewBox="0 0 12 12"><path d="M2 6l3 3 5-6" fill="none" stroke="#fff" stroke-width="1.6"/></svg></div><div class="head">Description</div><p class="txt">Clear value for each client group.</p></div>
  <div class="card" style="left:90px"><div class="icon"><svg width="12" height="12" viewBox="0 0 12 12"><circle cx="6" cy="6" r="4" fill="none" stroke="#fff" stroke-width="1.4"/></svg></div><div class="head">Description</div><p class="txt">Clear value for each client group.</p></div>
  <div class="card active" style="left:164px"><div class="icon"><svg width="12" height="12" viewBox="0 0 12 12"><path d="M6 1l1.5 3.2 3.5.4-2.6 2.3.8 3.4L6 8.6 2.8 10.3l.8-3.4L1 4.6l3.5-.4z" fill="#00ab8e"/></svg></div><div class="head">Description</div><p class="txt">Clear value for each client group.</p></div>
  <div class="card" style="left:238px"><div class="icon"><svg width="12" height="12" viewBox="0 0 12 12"><path d="M2 9h8M4 9V5M6 9V3M8 9V6" stroke="#fff" stroke-width="1.4"/></svg></div><div class="head">Description</div><p class="txt">Clear value for each client group.</p></div>
  <div class="brand light" style="left:280px;top:12px"><i></i>TIMREL</div>
  <div class="pager"><span></span><span></span><span></span></div>
</section>

<!-- 8 Services -->
<section class="slide col-b row-4">
  <svg class="wave" viewBox="0 0 336 183" preserveAspectRatio="none">
    <path d="M0 0H336V183H0Z" fill="#d9edf7"/>
    <path d="M0 0H336V30C250 42 120 18 0 34Z" fill="#0677ba"/>
  </svg>
  <div class="title" style="left:10px;top:8px">Our Awesome Services</div>
  <div class="svc" style="left:20px"><div class="icon"><svg width="10" height="10" viewBox="0 0 10 10"><path d="M5 1v8M1 5h8" stroke="#fff" stroke-width="1.4"/></svg></div><div class="label" style="position:static;margin-top:4px">Description</div><p class="txt" style="position:static">Race support and coaching.</p></div>
  <div class="svc" style="left:120px"><div class="icon"><svg width="10" height="10" viewBox="0 0 10 10"><circle cx="5" cy="5" r="3.5" fill="none" stroke="#fff" stroke-width="1.3"/></svg></div><div class="label" style="position:static;margin-top:4px">Description</div><p class="txt" style="position:static">Corporate sailing events.</p></div>
  <div class="svc" style="left:220px"><div class="icon"><svg width="10" height="10" viewBox="0 0 10 10"><path d="M1.5 5l2.5 2.5 4.5-5" fill="none" stroke="#fff" stroke-width="1.4"/></svg></div><div class="label" style="position:static;margin-top:4px">Description</div><p class="txt" style="position:static">Yacht care and delivery.</p></div>
  <div class="band"></div>
  <p class="txt light" style="left:120px;top:150px;width:190px">Tailored programs for owners and corporate teams.</p>
  <div class="brand light" style="left:280px;top:12px"><i></i>TIMREL</div>
  <div class="pager"><span></span><span></span><span></span></div>
</section>

<!-- 9 Project timeline -->
<section class="slide col-a row-5">
  <svg class="wave" viewBox="0 0 336 183" preserveAspectRatio="none">
    <path d="M0 0H336V183H0Z" fill="#e8f1f8"/>
    <path d="M0 0H336V30C250 42 120 18 0 34Z" fill="#0677ba"/>
    <path d="M0 140C90 125 200 150 336 132V183H0Z" fill="#cadeef"/>
    <path d="M20 128H316" stroke="#0a2f6b" stroke-width="1"/>
  </svg>
  <div class="title" style="left:10px;top:8px">Project Timeline</div>
  <div class="boat" role="img" aria-label="Sailboat silhouette" style="left:40px;top:90px;width:26px;height:38px"></div>
  <div class="boat" role="img" aria-label="Sailboat silhouette" style="left:105px;top:76px;width:34px;height:52px"></div>
  <div class="boat" role="img" aria-label="Sailboat silhouette" style="left:175px;top:62px;width:42px;height:66px"></div>
  <div class="boat" role="img" aria-label="Sailboat silhouette" style="left:250px;top:48px;width:50px;height:80px"></div>
  <div class="year" style="left:42px;top:80px">2020</div><div class="year" style="left:110px;top:66px">2021</div><div class="year" style="left:185px;top:52px">2022</div><div class="year" style="left:263px;top:38px">2023</div>
  <p class="txt" style="left:30px;top:138px;width:50px">Timeline 01</p><p class="txt" style="left:100px;top:138px;width:50px">Timeline 02</p><p class="txt" style="left:172px;top:138px;width:50px">Timeline 03</p><p class="txt" style="left:250px;top:138px;width:50px">Timeline 04</p>
  <div class="pager"><span></span><span></span><span></span></div>
</section>

<!-- 10 Get connected -->
<section class="slide col-b row-5">
  <svg class="wave" viewBox="0 0 336 183" preserveAspectRatio="none">
    <path d="M0 0H336V183H0Z" fill="#d9edf7"/>
    <path d="M0 0H336V30C250 42 120 18 0 34Z" fill="#0677ba"/>
    <path d="M205 40H336V183H205Z" fill="#00ab8e"/>
  </svg>
  <div class="title" style="left:10px;top:8px">Get Connected With Us</div>
  <div class="photo sail" role="img" aria-label="Racing catamarans with colourful sails" style="left:10px;top:40px;width:185px;height:120px"></div>
  <div class="contact-row" style="top:60px"><b><svg width="6" height="6" viewBox="0 0 6 6"><path d="M1 1l1.2-.2.6 1.4-.7.5a3 3 0 0 0 1.2 1.2l.5-.7 1.4.6L5 5C3 5.5.5 3 1 1z" fill="#00ab8e"/></svg></b>+00 123 456 789</div>
  <div class="contact-row" style="top:80px"><b><svg width="6" height="6" viewBox="0 0 6 6"><rect x=".5" y="1.2" width="5" height="3.6" fill="none" stroke="#00ab8e" stroke-width=".8"/></svg></b>hello@timrel.com</div>
  <div class="contact-row" style="top:100px"><b><svg width="6" height="6" viewBox="0 0 6 6"><path d="M3 .5a2 2 0 0 1 2 2C5 4 3 5.7 3 5.7S1 4 1 2.5a2 2 0 0 1 2-2z" fill="#00ab8e"/></svg></b>12 Harbour Road</div>
  <div class="contact-row" style="top:120px"><b><svg width="6" height="6" viewBox="0 0 6 6"><circle cx="3" cy="3" r="2.2" fill="none" stroke="#00ab8e" stroke-width=".8"/></svg></b>www.timrel.com</div>
  <div class="pager"><span></span><span></span><span></span></div>
</section>

<!-- 11 Thank you -->
<section class="slide col-a row-6">
  <div class="photo sea" role="img" aria-label="Yacht sailing under a clear sky" style="inset:0"></div>
  <svg class="wave" viewBox="0 0 336 183" preserveAspectRatio="none">
    <path d="M0 95C100 80 220 110 336 92V183H0Z" fill="#0054aa" opacity=".55"/>
  </svg>
  <div class="brand light" style="left:12px;top:12px;font-size:11px"><i></i>TIMREL</div>
  <div class="thanks">THANK YOU</div>
  <div class="site">WWW.TIMREL.COM</div>
</section>

<p class="board-note">I Jumped a few slides due to time</p>

</body>
</html>
```